A4 Hardback Menu Cover for classic British pub style establishment in Spain

The Brindlecott is a traditional British eatery in Southern Spain serving Pub/Bistro style classic dishes....

We require a new, simple, yet punchy design for our A4 hardback menu covers....

1. Designs should be submitted for both the outside FRONT and REAR cover....

2. A separate design for the INSIDE is to be included and can be much simpler. This is left to the designers discretion as long as it fits with the overall design....

3. Background colour to be along the lines of Stone/Light Grey, With the Design in a darker Grey/Black...

I have enclosed some attachments of the direction in which we would like to go, and are keen to stay along those lines....

Your design is for an evening menu where Steak, Lamb Shank, Chicken, homemade Pie and other classic pub style food all feature heavily. Some of the enclosed attachments feature fast food (we are not) and these are only supplied to show the style we feel would suit our business....

ATTACHED FILES...

FILES 1 & 2.... red/white petrol pump design is solely to show the actual product so you understand the end result...

FILE 3... is an idea for the inside cover....

FILES 6,7 13 and 14... are personal favourites....

The rest is up to you and your talent. Have some fun with it, and look forward to your submissions....

Hi all, there seems to be a slight issue with the deadline for this project. I posted it for 15 days (2 days ago), but unfortunately something has happened and is ending prematurely... If you are an interested designer please still work on this project as the deadline will be extended as soon as possible... Thanks in advance

Industry/Entity Type

Restaurant

Font styles to use
Serif
Sans Serif
Decorative
Script

Colors
e8e8e8
e0e0e0
d3d3d3
cacaca
b7b7b7
9d9d9d

Requirements
Must have
• Quality look and feel
Nice to have
• As attached files
• FILES 1 & 2.... red/white petrol pump design is solely to show the actual product so you understand the end result...
• FILE 3... is an idea for the inside cover....
Should not have
• Food Photography
• Cartoon style pics

```html
<!DOCTYPE html>
<html lang="en">
<head>
<meta charset="utf-8">
<title>The Brindlecott – Menu Cover</title>
<link rel="stylesheet" href="https://fonts.googleapis.com/css2?family=Mrs+Saint+Delafield&family=Tinos&display=swap">
<style>
  :root {
    --page: #ffffff;
    --stone: #e3e3e3;
    --botanical-core: rgba(150, 136, 148, 0.62);
    --botanical-mid: rgba(165, 152, 163, 0.42);
    --botanical-edge: rgba(185, 176, 184, 0.18);
    --rust: #c2684a;
    --ink: #555555;
  }
  html, body {
    margin: 0;
    padding: 0;
    width: 1200px;
    height: 1200px;
    overflow: hidden;
    background: var(--page);
  }
  .menu-cover {
    position: absolute;
    left: 176px;
    top: 0;
    width: 846px;
    height: 1200px;
    background: var(--stone);
    overflow: hidden;
  }
  .botanical {
    position: absolute;
    border-radius: 50%;
    background: radial-gradient(ellipse at center,
      var(--botanical-core) 0%,
      var(--botanical-mid) 38%,
      var(--botanical-edge) 62%,
      transparent 71%);
  }
  .botanical--berries-top-left { left: -40px; top: -30px; width: 320px; height: 560px; }
  .botanical--lily-top { left: 180px; top: -60px; width: 400px; height: 370px; }
  .botanical--rose-right { left: 505px; top: 95px; width: 350px; height: 340px; }
  .botanical--peony-left { left: -30px; top: 455px; width: 245px; height: 235px; }
  .botanical--berries-bottom-left { left: -40px; top: 660px; width: 450px; height: 580px; }
  .botanical--rosehips-middle { left: 380px; top: 625px; width: 370px; height: 410px; }
  .botanical--rosehips-right-edge { left: 705px; top: 735px; width: 170px; height: 220px; }
  .botanical--leaves-bottom { left: 440px; top: 985px; width: 340px; height: 260px; }

  .title-frame {
    position: absolute;
    left: 210px;
    top: 462px;
    width: 474px;
    height: 103px;
    border: 2px solid var(--rust);
    box-sizing: border-box;
  }
  .title-script {
    position: absolute;
    left: 250px;
    top: 478px;
    margin: 0;
    font-family: "Mrs Saint Delafield", cursive;
    font-weight: 400;
    font-size: 96px;
    line-height: 1;
    color: var(--rust);
    letter-spacing: 30px;
  }
  .venue-name {
    position: absolute;
    right: 171px;
    top: 580px;
    margin: 0;
    font-family: "Tinos", "Times New Roman", serif;
    font-weight: 400;
    font-size: 45px;
    line-height: 1;
    color: var(--ink);
    letter-spacing: 0.5px;
    white-space: nowrap;
  }
</style>
</head>
<body>
  <main class="menu-cover">
    <div class="botanical botanical--berries-top-left" role="img" aria-label="Watercolour sprigs of grey-mauve berries"></div>
    <div class="botanical botanical--lily-top" role="img" aria-label="Watercolour lily blossom in soft grey-mauve"></div>
    <div class="botanical botanical--rose-right" role="img" aria-label="Watercolour ranunculus flower with stem"></div>
    <div class="botanical botanical--peony-left" role="img" aria-label="Watercolour peony bud with leaves"></div>
    <div class="botanical botanical--berries-bottom-left" role="img" aria-label="Watercolour round berries on long stems"></div>
    <div class="botanical botanical--rosehips-middle" role="img" aria-label="Watercolour rosehips on a leafy branch"></div>
    <div class="botanical botanical--rosehips-right-edge" role="img" aria-label="Watercolour rosehips at the edge of the cover"></div>
    <div class="botanical botanical--leaves-bottom" role="img" aria-label="Watercolour eucalyptus leaves"></div>

    <div class="title-frame"></div>
    <h1 class="title-script">Menu</h1>
    <p class="venue-name">THE BRINDLECOTT</p>
  </main>
</body>
</html>
```